Need a book cover design for a Lumora Book

Book has a long title and sub title so lots of words to fit on the cover.

I can be flexible a bit with the sub title due to the length of it but ideally i can get a design that takes everything.

Here is the title:

Tidal Geology: The Roots of Erosion, Sedimentation, and Canyon Forming

Sub Title/Heading
An Easy Primer on Coastal Cliffs, Dune Drift, River Beds, and Delta Mapping Methods

```html
<!DOCTYPE html>
<html lang="en">
<head>
<meta charset="utf-8">
<title>Tidal Geology – Book Cover</title>
<link rel="stylesheet" href="https://fonts.googleapis.com/css2?family=Oswald:wght@300&family=Barlow:wght@400&family=IBM+Plex+Mono:wght@300&display=swap">
<style>
  :root {
    --navy-deep: #07121f;
    --navy: #0d2236;
    --teal: #15485a;
    --cyan: #2fd6ef;
    --cyan-glow: #35c8ec;
    --white: #f4f7fa;
  }
  html, body {
    margin: 0;
    padding: 0;
    width: 679px;
    height: 1200px;
    overflow: hidden;
    background: var(--navy-deep);
  }
  .cover {
    position: relative;
    width: 679px;
    height: 1200px;
    overflow: hidden;
    color: var(--white);
  }
  .cover-art {
    position: absolute;
    inset: 0;
    background:
      radial-gradient(ellipse 70% 18% at 50% 102%, rgba(53,200,236,0.9) 0%, rgba(53,200,236,0.35) 45%, transparent 75%),
      radial-gradient(ellipse 55% 30% at 10% 85%, rgba(38,150,190,0.55) 0%, transparent 70%),
      radial-gradient(ellipse 60% 35% at 55% 45%, rgba(40,110,130,0.45) 0%, transparent 70%),
      radial-gradient(ellipse 50% 25% at 90% 55%, rgba(40,120,140,0.35) 0%, transparent 70%),
      linear-gradient(180deg, var(--navy-deep) 0%, var(--navy) 35%, var(--teal) 60%, var(--navy) 78%, #0f3550 100%);
  }
  .series-title {
    position: absolute;
    top: 148px;
    left: 0;
    width: 100%;
    margin: 0;
    text-align: center;
    font-family: "Oswald", sans-serif;
    font-weight: 300;
    font-size: 76px;
    line-height: 1;
    letter-spacing: 0.02em;
    color: var(--cyan);
  }
  .title-lead {
    position: absolute;
    top: 252px;
    left: 0;
    width: 100%;
    text-align: center;
    font-family: "Barlow", sans-serif;
    font-size: 21px;
    letter-spacing: 0.5em;
    text-indent: 0.5em;
  }
  .main-title {
    position: absolute;
    top: 352px;
    left: 0;
    width: 100%;
    text-align: center;
    font-family: "Barlow", sans-serif;
    font-weight: 400;
    font-size: 48px;
    line-height: 69px;
    letter-spacing: 0.14em;
  }
  .main-title span { display: block; }
  .main-title .with-and {
    display: flex;
    justify-content: center;
    align-items: center;
  }
  .and-vertical {
    display: inline-block;
    font-size: 14px;
    letter-spacing: 0.1em;
    line-height: 1;
    writing-mode: vertical-rl;
    margin-right: 6px;
  }
  .subtitle {
    position: absolute;
    top: 793px;
    left: 0;
    width: 100%;
    text-align: center;
    font-family: "IBM Plex Mono", monospace;
    font-weight: 300;
    font-size: 24px;
    line-height: 32px;
    letter-spacing: 0.08em;
  }
  .subtitle span { display: block; }
</style>
</head>
<body>
  <main class="cover">
    <div class="cover-art" role="img" aria-label="Dark deep-blue abstract backdrop with faint scribbled formulas, sweeping particle waves and a glowing cyan wave along the bottom"></div>

    <h1 class="series-title">TIDAL GEOLOGY</h1>
    <div class="title-lead">THE ROOTS OF</div>
    <h2 class="main-title">
      <span>EROSION</span>
      <span>SEDIMENTATION</span>
      <span class="with-and"><span class="and-vertical">AND</span>CANYON FORMING</span>
    </h2>

    <p class="subtitle">
      <span>An Easy Primer On</span>
      <span>Coastal Cliffs</span>
      <span>Dune Drift</span>
      <span>River Beds</span>
      <span>And Delta Mapping Methods</span>
    </p>
  </main>
</body>
</html>
```